Copper Ridge Garage Door Sales & Repair needs a Business Card Design

I need a business card design to go with our new business logo that was created a few months ago.

Copper Ridge Garage Door specializes in selling and installing new garage doors, and new garage door openers. We also take care of all repairs to existing garage doors and garage door openers. All makes and models.

Target Market(s)

Home-owners, renters, anyone who lives in a house and has a garage. Residential and commercial garages.

Industry/Entity Type

Home Improvement

Contact Information for Business Card

I would like the business cards to have rounded corners and be double-sided. My old logo is still on my website at www.copperridgegarage.example. If I was going to incorporate a secondary color on the business cards, I think that orange is a good choice (especially since blue and orange are the colors of our Tulsa Comets), but I'm not opposed to seeing a different color if another color works better with my logo colors. I have two logo colors. One designed for a white background and one designed for a darker background. I'm not opposed to using both. Maybe a dark background with the white logo on one side, and a white background with the other logo color on the other side.

My business is a small, locally owned business that I am trying to grow. But I would like my business cards to look very professional. Like we have been in business for a long time. I like traditional to modern looking cards. Just something bold and memorable. My full company name is Copper Ridge Garage Door Sales & Repair. But you can just do COPPER RIDGE GARAGE DOOR, if that works better.

Font styles to use
Serif
Script

Requirements
Must have
• Rounded corners
• Double-sided
• 3-D Elements. Layering of some sort (a sketch of a garage door or a 3rd color (orange) brought in some how. I really like watermarks.
• Matte cards that you can write on.
• White on one side. (Or the lighter blue in my logo). Darker blue logo color on the other side.
• I would like our tag line on the cards somewhere... "For All Your Garage Door Needs".
• I would also like "Call For a FREE Estimate" by the phone number.
• And "Serving the Greater Metro Denver Area" somewhere on the card as well.
Nice to have
• Refer to "Business Card Details" above.

```html
<!DOCTYPE html>
<html lang="en">
<head>
<meta charset="utf-8">
<title>Copper Ridge Garage Door – Business Card</title>
<link rel="stylesheet" href="https://fonts.googleapis.com/css2?family=Open+Sans:wght@400;600;700&display=swap">
<style>
  :root {
    --stage: #2b2b2c;
    --copper-light: #e7a658;
    --copper-mid: #d18a3c;
    --copper-deep: #b8691f;
    --ink: #050505;
    --paper: #ffffff;
    --accent: #f7941d;
  }
  * { box-sizing: border-box; margin: 0; padding: 0; }
  html, body { width: 1200px; height: 900px; overflow: hidden; }
  body {
    background: var(--stage);
    font-family: "Open Sans", Arial, sans-serif;
    position: relative;
  }
  .card {
    position: absolute;
    width: 600px;
    height: 345px;
    border-radius: 22px;
    overflow: hidden;
    box-shadow: 0 14px 30px rgba(0,0,0,0.45);
  }

  /* Front */
  .card--front { left: 110px; top: 80px; }
  .front-scene {
    position: absolute; inset: 0;
    background: linear-gradient(180deg, var(--copper-light) 0%, var(--copper-mid) 45%, var(--copper-deep) 100%);
  }
  .front-brand {
    position: absolute; left: 70px; top: 130px;
    display: flex; align-items: center; gap: 14px;
    color: var(--paper);
  }
  .brand-dot {
    width: 26px; height: 26px; border-radius: 50%;
    border: 3px solid var(--paper);
  }
  .brand-name {
    font-weight: 700; font-size: 24px; line-height: 1.15; letter-spacing: 1px;
    text-transform: uppercase;
  }
  .front-tagline {
    position: absolute; left: 330px; top: 160px;
    color: var(--paper); font-size: 14px; font-weight: 600; letter-spacing: .3px;
  }
  .front-watermark {
    position: absolute; right: 30px; top: 50px;
    font-weight: 700; font-size: 38px; line-height: 1.1; text-align: center;
    color: rgba(255,255,255,0.12); text-transform: uppercase;
  }

  /* Back */
  .card--back { left: 490px; top: 470px; background: var(--ink); }
  .side-band {
    position: absolute; left: 38px; top: 0; bottom: 0; width: 74px;
    background: linear-gradient(180deg, var(--paper) 0 42%, var(--ink) 42% 50%, var(--accent) 50% 100%);
  }
  .band-brand {
    position: absolute; left: 34px; top: 92px;
    width: 82px; height: 82px; border-radius: 50%;
    background: var(--ink); border: 3px solid var(--paper);
    display: flex; align-items: center; justify-content: center; text-align: center;
    color: var(--paper); font-weight: 700; font-size: 10px; line-height: 1.2;
    text-transform: uppercase;
  }
  .person {
    position: absolute; right: 40px; top: 28px; text-align: right;
  }
  .person-name { color: var(--paper); font-weight: 700; font-size: 19px; letter-spacing: 1.5px; }
  .person-role { color: var(--accent); font-size: 12px; font-weight: 600; }
  .back-watermark {
    position: absolute; right: 50px; top: 90px;
    font-weight: 700; font-size: 34px; line-height: 1.1; text-align: center;
    color: rgba(255,255,255,0.07); text-transform: uppercase;
  }
  .contact {
    position: absolute; left: 150px; top: 186px;
    color: var(--paper); font-size: 12.5px; line-height: 1.35;
  }
  .contact-address { margin-bottom: 8px; }
  .contact-list { list-style: none; }
  .contact-list li { display: flex; align-items: center; gap: 8px; }
  .contact-list svg { width: 11px; height: 11px; flex: none; }
  .service-area {
    position: absolute; right: 36px; bottom: 26px;
    color: var(--accent); font-weight: 600; font-size: 14px;
  }
</style>
</head>
<body>

<section class="card card--front" aria-label="Card front">
  <div class="front-scene" role="img" aria-label="Hazy layered mountain ridges in copper and amber tones"></div>
  <div class="front-watermark">Copper Ridge<br>Garage Door</div>
  <div class="front-brand">
    <span class="brand-dot"></span>
    <span class="brand-name">Copper Ridge<br>Garage Door</span>
  </div>
  <p class="front-tagline">For All Your Garage Door Needs</p>
</section>

<section class="card card--back" aria-label="Card back">
  <div class="side-band"></div>
  <div class="band-brand">Copper<br>Ridge<br>Garage</div>
  <div class="back-watermark">Copper Ridge<br>Garage Door</div>
  <div class="person">
    <p class="person-name">DANA MERCER</p>
    <p class="person-role">Director</p>
  </div>
  <div class="contact">
    <p class="contact-address">4120 Ridgeline Ave<br>Lakewood, CO 80226</p>
    <ul class="contact-list">
      <li><svg viewBox="0 0 12 12" aria-hidden="true"><path d="M2.5 1h2l1 3-1.3 1a6 6 0 0 0 2.8 2.8l1-1.3 3 1v2a1 1 0 0 1-1 1A9 9 0 0 1 1.5 2a1 1 0 0 1 1-1z" fill="var(--accent)"/></svg>555-014-2290 (FREE)</li>
      <li><svg viewBox="0 0 12 12" aria-hidden="true"><rect x="1" y="2.5" width="10" height="7" fill="none" stroke="var(--accent)" stroke-width="1.2"/><path d="M1 2.5l5 4 5-4" fill="none" stroke="var(--accent)" stroke-width="1.2"/></svg>info@copperridgegarage.example</li>
      <li><svg viewBox="0 0 12 12" aria-hidden="true"><circle cx="6" cy="6" r="5" fill="none" stroke="var(--accent)" stroke-width="1.2"/><path d="M1 6h10M6 1c-2.5 3-2.5 7 0 10M6 1c2.5 3 2.5 7 0 10" fill="none" stroke="var(--accent)" stroke-width="1"/></svg>www.copperridgegarage.example</li>
    </ul>
  </div>
  <p class="service-area">Serving the Greater Metro Denver Area</p>
</section>

</body>
</html>
```